Summit Grading a Builders LLC business card

My current business card is very plain. it has my logo and contact information. I woud like something that stands out from the rest. please take a look at my website to see about my company.

Compayt Name - Summit Grading And Builders
Owner - Martin Kowalczyk
Business Address
Business Website - www.summitgradingandbuilders.example
Email - Summitgradingandbuilders@mailbox.example
Phone - 555-214-7390
Fax - 555-806-3127

Target Market(s)

Everyone age tang is 18 - 85

Industry/Entity Type

Business

Contact Information for Business Card

Nice and professional all in one.

Font styles to use
Serif
Other font styles liked:
• Up to you

Requirements
Must have
• All contact info. The design is up to you.
Nice to have
• All the contact info the design is up to you
Should not have
• I don't have any

```html
<!DOCTYPE html>
<html lang="en">
<head>
<meta charset="utf-8">
<title>Summit Grading a Builders LLC – Business Card</title>
<link rel="stylesheet" href="https://fonts.googleapis.com/css2?family=Tinos:wght@400;700&display=swap">
<style>
  :root {
    --page-bg: #e6e0d8;
    --card-light: #f4f3f1;
    --card-mid: #dcd9d6;
    --ink: #1c1c1c;
    --ink-soft: #3a3a3a;
    --label-grey: #8a8a8a;
    --logo-grey: #666666;
    --rule: #8f8f8f;
    --band-grey: #a9a7a5;
    --band-dark: #1a1a1a;
    --placeholder: #c9c6c3;
  }
  * { margin: 0; padding: 0; box-sizing: border-box; }
  html, body { width: 1200px; height: 970px; overflow: hidden; }
  body {
    background: var(--page-bg);
    font-family: "Tinos", "Times New Roman", serif;
    position: relative;
  }
  .business-card {
    position: absolute;
    left: 80px; top: 189px;
    width: 1040px; height: 592px;
    background:
      radial-gradient(ellipse 300px 120px at 420px 500px, rgba(214,150,160,0.35), transparent 70%),
      linear-gradient(115deg, var(--card-light) 0%, #ecebe9 45%, var(--card-mid) 100%);
    box-shadow: 0 10px 30px rgba(0,0,0,0.18);
    overflow: hidden;
  }
  .company-name {
    position: absolute;
    left: 55px; top: 72px;
    font-weight: 700;
    font-size: 56px;
    line-height: 68px;
    color: var(--logo-grey);
    letter-spacing: 1px;
  }
  .company-name .first-line { padding-left: 33px; }
  .owner-block {
    position: absolute;
    right: 58px; top: 288px;
    text-align: right;
  }
  .owner-name { font-weight: 700; font-size: 34px; color: var(--ink); line-height: 38px; }
  .owner-title { font-size: 26px; color: var(--label-grey); line-height: 30px; }
  .divider {
    position: absolute;
    left: 55px; top: 349px;
    width: 836px; height: 1.5px;
    background: var(--rule);
  }
  .contact-list {
    position: absolute;
    left: 55px; top: 372px;
    list-style: none;
    font-size: 27px;
    color: var(--ink-soft);
    line-height: 42.5px;
  }
  .contact-label { color: var(--label-grey); }
  .partner-marks {
    position: absolute;
    left: 725px; top: 458px;
    display: flex;
    gap: 24px;
  }
  .partner-mark {
    width: 70px; height: 72px;
    border-radius: 8px;
    background: var(--placeholder);
  }
  .card-band {
    position: absolute;
    left: 0; bottom: 0;
    width: 1040px; height: 38px;
  }
</style>
</head>
<body>
  <div class="business-card">
    <div class="company-name"><span class="first-line">SUMMIT GRADING</span><br>&amp; BUILDERS LLC</div>

    <div class="owner-block">
      <div class="owner-name">Martin Kowalczyk</div>
      <div class="owner-title">Owner</div>
    </div>

    <div class="divider"></div>

    <ul class="contact-list">
      <li>PO BOX 123 your address, 2nd street london ,USA</li>
      <li><span class="contact-label">P:</span> 555-214-7390 | <span class="contact-label">F:</span> 555-806-3127</li>
      <li><span class="contact-label">E:</span> Summitgradingandbuilders@mailbox.example</li>
      <li>www.summitgradingandbuilders.example</li>
    </ul>

    <div class="partner-marks">
      <div class="partner-mark" role="img" aria-label="Partner certification mark"></div>
      <div class="partner-mark" role="img" aria-label="Partner service award mark"></div>
      <div class="partner-mark" role="img" aria-label="Partner rating mark"></div>
    </div>

    <svg class="card-band" viewBox="0 0 1040 38" preserveAspectRatio="none" aria-hidden="true">
      <polygon points="0,0 620,0 642,38 0,38" fill="var(--band-grey)" opacity="0.75"/>
      <polygon points="626,15 1040,15 1040,38 642,38" fill="var(--band-dark)"/>
    </svg>
  </div>
</body>
</html>
```